BRAVELUX Program Cover

Every year, we host an annual conference for educators who teach in afterschool in the Southwest. This year, we are renaming the conference to BRAVELUX 2014 (stands for Beyond-Bell-Hours Learning Summit). The theme of our conference is made up of three verbs: Innovate, Collaborate, & Thrive. We are looking for a program cover that is creative and yet visually appealing to an audience that ranges from Millennials to Baby Boomers. It needs to convey the three verbs and also brand the conference with the new name. We like the colors Blue and Green as our previous programs have been red, gold, yellow, and orange. Our audience teaches kids from K - 12, but likes to be treated as professionals (not the typical school clipart stuff). The conference is hosted at the Ft. Worth Calloway Lodge from July 23rd to July 24th, 2014. The program cover will set the tone for all conference materials (i.e. color scene, potential logo, etc...).

Target Market(s)

The target audience is participants of the conference. The age ranges from 25 to 60, but they are all either teachers, social workers, or educational administrators. All have a Bachelor's Degree or higher. While they are professionals, they also like to have fun.

Industry/Entity Type

Graphic Design

Requirements
Must have
• BRAVELUX must be prevalent and tagged with Beyond-Bell-Hours Learning Summit so that people know what it stands for.
Should not have
• The design should be clean with zero clipart.

```html
<!DOCTYPE html>
<html lang="en">
<head>
<meta charset="utf-8">
<title>BRAVELUX 2014 Program Cover</title>
<link rel="stylesheet" href="https://fonts.googleapis.com/css2?family=Russo+One&family=Source+Sans+3:wght@400&display=swap">
<style>
  :root {
    --sky-blue: #00aeef;
    --leaf-green: #8dc63f;
    --paper: #ffffff;
    --ink: #3a3a3a;
    --ink-dark: #1e1e1e;
  }
  html, body {
    margin: 0;
    padding: 0;
    width: 1200px;
    height: 999px;
    overflow: hidden;
    background: var(--sky-blue);
  }
  .cover-stage { display: block; width: 1200px; height: 999px; }
  .brand-title, .brand-year {
    font-family: "Russo One", "Arial Black", sans-serif;
    fill: var(--sky-blue);
  }
  .tagline, .event-details, .summit-name {
    font-family: "Source Sans 3", "Myriad Pro", Arial, sans-serif;
  }
  .tagline { fill: var(--ink); font-size: 31px; }
  .event-details { fill: var(--ink-dark); font-size: 31px; }
  .summit-name { fill: var(--paper); font-size: 30px; }
</style>
</head>
<body>
<svg class="cover-stage" width="1200" height="999" viewBox="0 0 1200 999" xmlns="http://www.w3.org/2000/svg">
  <defs>
    <clipPath id="page-clip"><rect x="242" y="37" width="716" height="925"/></clipPath>
    <linearGradient id="tone-row" x1="0" y1="0" x2="1" y2="1">
      <stop offset="0" stop-color="#e8e4dc"/>
      <stop offset="0.3" stop-color="#e9c9a0"/>
      <stop offset="0.5" stop-color="#d98a3c"/>
      <stop offset="0.7" stop-color="#d67a92"/>
      <stop offset="1" stop-color="#2f9ccf"/>
    </linearGradient>
    <linearGradient id="tone-paint" x1="0" y1="0" x2="1" y2="1">
      <stop offset="0" stop-color="#e9d6a8"/>
      <stop offset="0.35" stop-color="#c9662e"/>
      <stop offset="0.6" stop-color="#d8336f"/>
      <stop offset="0.85" stop-color="#c7342e"/>
      <stop offset="1" stop-color="#e8d8c4"/>
    </linearGradient>
    <linearGradient id="tone-bricks" x1="0" y1="0" x2="0" y2="1">
      <stop offset="0" stop-color="#dfe4ea"/>
      <stop offset="0.3" stop-color="#f3d27a"/>
      <stop offset="0.55" stop-color="#3f9a45"/>
      <stop offset="0.75" stop-color="#f2dc2e"/>
      <stop offset="1" stop-color="#3b4fbf"/>
    </linearGradient>
  </defs>

  <rect class="cover-page" x="242" y="37" width="716" height="925" fill="var(--paper)"/>

  <text class="brand-title" x="266" y="188" font-size="106" textLength="672" lengthAdjust="spacingAndGlyphs">BRAVELUX</text>

  <text class="tagline" x="936" y="250" text-anchor="end">Innovate, Collaborate, &amp; Thrive</text>

  <rect class="theme-band" x="242" y="283" width="716" height="455" fill="var(--leaf-green)"/>

  <g class="photo-circles" clip-path="url(#page-clip)">
    <circle role="img" aria-label="Photo of smiling schoolchildren sitting in a row" cx="370" cy="370" r="152" fill="url(#tone-row)" stroke="var(--paper)" stroke-width="4"/>
    <circle role="img" aria-label="Photo of children painting at a classroom table" cx="577" cy="482" r="127" fill="url(#tone-paint)" stroke="var(--paper)" stroke-width="4"/>
    <circle role="img" aria-label="Photo of a toddler building with colourful toy bricks" cx="387" cy="609" r="127" fill="url(#tone-bricks)" stroke="var(--paper)" stroke-width="4"/>
  </g>

  <text class="event-details" text-anchor="end">
    <tspan x="921" y="674">Ft. Worth Calloway Lodge from</tspan>
    <tspan x="916" y="712">July 23rd to July 24th, 2014</tspan>
  </text>

  <text class="brand-year" x="420" y="865" font-size="100" textLength="392" lengthAdjust="spacingAndGlyphs">2014</text>

  <rect class="summit-band" x="242" y="900" width="716" height="40" fill="var(--sky-blue)"/>
  <text class="summit-name" x="600" y="930" text-anchor="middle">Beyond-Bell-Hours Learning Summit</text>
</svg>
</body>
</html>
```